Libro Sumemos Juntos - Crowdfunding Real Estate

Realizar la Portada de mi primer libro ¡Sumemos juntos! - CROWDFUNDING Y OTROS CONSEJOS PARA INVERTIR CON ÉXITO EN LA NUEVA ERA INMOBILIARIA.

Target Market(s)

Chileans between 25 and 45 years of middle class

Industry/Entity Type

Crowdfunding

Requirements
Must have
• Attractive cover that allows to sell as many units as possible. On the back of the cover a description of me (the author). In the cover comments of people who recommend the book.
Nice to have
• Include a chart of the Sumemos Model Together applied to the Real Estate Crowdfunding, which is what the book is about

```html
<!DOCTYPE html>
<html lang="es">
<head>
<meta charset="utf-8">
<title>Sumemos Juntos – Portada</title>
<link href="https://fonts.googleapis.com/css2?family=Oswald:wght@500;600;700&display=swap" rel="stylesheet">
<style>
  :root {
    --bg-top: #f4f4f4;
    --bg-bottom: #d9d9d9;
    --cover: #ffffff;
    --ink: #161616;
    --accent: #34a6dc;
    --rope: #4fb3d3;
    --skin: #e9b89a;
    --suit-dark: #3a3638;
    --suit-light: #c9d3da;
  }
  * { margin: 0; padding: 0; box-sizing: border-box; }
  html, body {
    width: 1111px;
    height: 1200px;
    overflow: hidden;
  }
  body {
    background: linear-gradient(180deg, var(--bg-top), var(--bg-bottom));
    font-family: "Oswald", "Arial Narrow", sans-serif;
    position: relative;
  }
  .book-cover {
    position: absolute;
    left: 195px;
    top: 50px;
    width: 720px;
    height: 1100px;
    background: var(--cover);
    box-shadow: 0 10px 40px rgba(0,0,0,0.18);
    overflow: hidden;
  }
  .cover-photo {
    position: absolute;
    left: 0;
    top: 0;
    width: 100%;
    height: 820px;
    background:
      radial-gradient(ellipse 34% 36% at 50% 52%, var(--cover) 70%, rgba(255,255,255,0) 100%),
      radial-gradient(ellipse 44% 46% at 50% 52%, rgba(79,179,211,0.9) 78%, rgba(79,179,211,0) 100%),
      radial-gradient(ellipse 62% 60% at 50% 50%, rgba(233,184,154,0.95) 60%, rgba(233,184,154,0) 100%),
      linear-gradient(135deg, var(--suit-light) 0%, #f2f2f2 35%, #f2f2f2 65%, var(--suit-dark) 100%);
  }
  .cover-photo::after {
    content: "";
    position: absolute;
    left: 0; right: 0; bottom: 0;
    height: 200px;
    background: linear-gradient(180deg, rgba(255,255,255,0), var(--cover));
  }
  .cover-title {
    position: absolute;
    top: 300px;
    left: 0;
    width: 100%;
    text-align: center;
    text-transform: uppercase;
    line-height: 1;
  }
  .title-line-1 {
    display: block;
    font-weight: 600;
    font-size: 86px;
    color: var(--ink);
    letter-spacing: 1px;
  }
  .title-line-2 {
    display: block;
    font-weight: 700;
    font-size: 120px;
    color: var(--accent);
    margin-top: 2px;
    letter-spacing: 1px;
  }
  .author-name {
    display: block;
    font-weight: 600;
    font-size: 42px;
    color: var(--ink);
    margin-top: 14px;
  }
  .cover-subtitle {
    position: absolute;
    top: 840px;
    left: 0;
    width: 100%;
    text-align: center;
    text-transform: uppercase;
    color: var(--ink);
    line-height: 1.18;
  }
  .subtitle-lead {
    display: block;
    font-weight: 700;
    font-size: 46px;
    margin-bottom: 6px;
  }
  .subtitle-rest {
    display: block;
    font-weight: 600;
    font-size: 33px;
  }
</style>
</head>
<body>
  <main class="book-cover">
    <div class="cover-photo" role="img" aria-label="Fotografía de manos de personas en traje sosteniendo una cuerda azul con forma de casa"></div>

    <h1 class="cover-title">
      <span class="title-line-1">Sumemos</span>
      <span class="title-line-2">Juntos</span>
      <span class="author-name">Nombre Autor</span>
    </h1>

    <p class="cover-subtitle">
      <span class="subtitle-lead">Crowdfunding</span>
      <span class="subtitle-rest">y otros consejos para invertir con éxito<br>en la nueva era inmobiliaria</span>
    </p>
  </main>
</body>
</html>
```